Conservative, Modern and Sharp Builder Business card

Hi there,
We would like to update our existing business card.
I have attached photos of existing business card, logo and van sign.

I would like the business card to also list what we do :
Renovation • New Build • Alteration
Extension • Bathroom • Maintenance.(Seperated by dots)

Contact number : 021 0483 0752
(With that exact spacing)

Ideally when people looking from about 2-3 metres, they know that it is a builder’s business card

Open to suggestions on fonts, layout, style of business card

PLEASE ONLY SUBMIT YOUR BEST OR MAX 3 DESIGNS FOR EACH DESIGNER

Thanks

Construction. Renovation

Details should be the same as the existing card. And addition of what we do.

• The new business card must not have the same layout as our existing one. Thanks

```html
<!DOCTYPE html>
<html lang="en">
<head>
<meta charset="utf-8">
<title>Keelson Build – Business Card</title>
<link href="https://fonts.googleapis.com/css2?family=Inter:wght@400;700;800&display=swap" rel="stylesheet">
<style>
  :root {
    --stage: #3d3d3d;
    --card-light: #f4f4f5;
    --card-dark: #0b0b0c;
    --ink: #111111;
    --ink-soft: #555555;
    --paper-text: #f2f2f2;
    --mark-grey: #8a8a8a;
  }
  * { margin: 0; padding: 0; box-sizing: border-box; }
  html, body {
    width: 1200px; height: 799px; overflow: hidden;
    background: var(--stage);
    font-family: "Inter", Arial, sans-serif;
  }
  .stage {
    position: relative; width: 1200px; height: 799px;
    display: flex; align-items: center; justify-content: center; gap: 60px;
  }
  .card {
    position: relative; width: 500px; height: 286px;
    border-radius: 22px; overflow: hidden;
    box-shadow: 0 18px 40px rgba(0,0,0,0.45);
  }
  /* Front */
  .card--front { background: var(--card-light); color: var(--ink); }
  .brand {
    position: absolute; top: 62px; left: 250px;
    display: flex; align-items: center; gap: 10px;
  }
  .brand__square { width: 14px; height: 14px; background: var(--ink); }
  .brand__name { font-weight: 800; font-size: 30px; letter-spacing: -0.5px; color: var(--ink); }
  .contact { position: absolute; left: 40px; bottom: 34px; }
  .contact__name { font-weight: 700; font-size: 17px; }
  .contact__role { font-size: 10.5px; color: var(--ink-soft); margin-bottom: 12px; }
  .contact__list { list-style: none; }
  .contact__item {
    display: flex; align-items: center; gap: 8px;
    font-size: 12px; line-height: 17px; color: var(--ink);
  }
  .contact__icon { width: 10px; height: 10px; flex: none; }
  /* Back */
  .card--back {
    background: linear-gradient(135deg, #1a1a1c 0%, var(--card-dark) 55%);
    color: var(--paper-text);
  }
  .back-brand {
    position: absolute; top: 82px; left: 0; right: 0;
    display: flex; align-items: center; justify-content: center; gap: 14px;
  }
  .back-brand__square { width: 18px; height: 18px; background: var(--mark-grey); }
  .back-brand__name { font-weight: 800; font-size: 44px; letter-spacing: -1px; color: var(--paper-text); }
  .services {
    position: absolute; left: 0; right: 0; bottom: 48px;
    text-align: center; font-size: 15.5px; line-height: 22px; color: var(--paper-text);
  }
  .services__sep {
    display: inline-block; width: 6px; height: 6px; margin: 0 6px 2px;
    background:
      linear-gradient(var(--paper-text),var(--paper-text)) 0 0/2px 2px no-repeat,
      linear-gradient(var(--paper-text),var(--paper-text)) 4px 0/2px 2px no-repeat,
      linear-gradient(var(--paper-text),var(--paper-text)) 0 4px/2px 2px no-repeat,
      linear-gradient(var(--paper-text),var(--paper-text)) 4px 4px/2px 2px no-repeat;
  }
</style>
</head>
<body>
<main class="stage">
  <section class="card card--front">
    <div class="brand">
      <span class="brand__square"></span>
      <span class="brand__name">Keelson Build</span>
    </div>
    <div class="contact">
      <p class="contact__name">Daniel Moreau</p>
      <p class="contact__role">Residential Builder</p>
      <ul class="contact__list">
        <li class="contact__item">
          <svg class="contact__icon" viewBox="0 0 10 10"><path d="M2 0.5 L4 2.8 L3 4 Q4.5 6 6 7 L7.2 6 L9.5 8 L8 9.5 Q3 8.5 0.5 2 Z" fill="#111"/></svg>
          021 0483 0752
        </li>
        <li class="contact__item">
          <svg class="contact__icon" viewBox="0 0 10 10"><rect x="0.5" y="2" width="9" height="6.5" fill="#111"/><path d="M0.8 2.3 L5 5.6 L9.2 2.3" stroke="#f4f4f5" stroke-width="0.9" fill="none"/></svg>
          hello@keelsonbuild.co.nz
        </li>
        <li class="contact__item">
          <svg class="contact__icon" viewBox="0 0 10 10"><circle cx="5" cy="5" r="4.6" fill="#111"/><path d="M0.6 5 H9.4 M5 0.5 Q2.5 5 5 9.5 M5 0.5 Q7.5 5 5 9.5" stroke="#f4f4f5" stroke-width="0.7" fill="none"/></svg>
          www.KeelsonBuild.nz
        </li>
        <li class="contact__item">
          <svg class="contact__icon" viewBox="0 0 10 10"><circle cx="5" cy="5" r="4.6" fill="#111"/><circle cx="5" cy="5" r="2" fill="none" stroke="#f4f4f5" stroke-width="0.9"/></svg>
          KeelsonBuild.nz
        </li>
      </ul>
    </div>
  </section>

  <section class="card card--back">
    <div class="back-brand">
      <span class="back-brand__square"></span>
      <span class="back-brand__name">Keelson Build</span>
    </div>
    <p class="services">
      Renovation<span class="services__sep"></span>New Build<span class="services__sep"></span>Alteration<br>
      Extension<span class="services__sep"></span>Bathroom<span class="services__sep"></span>Maintenance.
    </p>
  </section>
</main>
</body>
</html>
```